School District In Need of Powerful Presentation

Create a modern PPT design template -- standard and widescreen -- for the Pell RU-8K school district inspired by its logo. The presentation should be a modern projection of 21st education that excites the people who view it. The school district is located in a rural farming community with a view of the rocky mountains to its west (check out this picture www.campsiteatmarblefork.example/AnimatedImages/HomeGallery/000MountainScene.jpg). People in this community want quality education for their children with opportunities for them to be successful after they graduate.

Target Market(s)

The Harbrook and Denning communities in Northern Colorado

Industry/Entity Type

Education

Font styles to use
Sans Serif

Colors
ec1f27
3176b5
acd036
fece3e
f78f20

Requirements
Must have
• The name of the school district:
• Pell County School District RU-8K Harbrook-Denning
• Website address: www.pellru8k.example/
• Email: listen@pellru8k.example
Nice to have
• A couple of color options including their current color scheme: red, gold, black
• Placeholder for pictures of students and teachers
Should not have
• Please do not use the full logo in it's current for, but you may use elements of the logo.

```html
<!DOCTYPE html>
<html lang="en">
<head>
<meta charset="utf-8">
<title>Pell County Schools Presentation Template</title>
<link href="https://fonts.googleapis.com/css2?family=Raleway:wght@300;400;600;700&display=swap" rel="stylesheet">
<style>
:root{
  --red:#ec1f27;
  --blue:#3176b5;
  --green:#acd036;
  --yellow:#fece3e;
  --orange:#f7a823;
  --teal:#27b9d3;
  --ink:#333;
  --muted:#a3a3a3;
  --footer:#b0121a;
  --footer-dark:#6e0a10;
}
*{box-sizing:border-box;margin:0;padding:0}
html,body{width:1039px;height:1200px;overflow:hidden;background:#e9e9e9;font-family:"Raleway",sans-serif}
.deck{display:grid;grid-template-columns:repeat(3,345px);grid-auto-rows:198px;gap:2px;width:1039px;height:1200px}
.slide{position:relative;background:#fff;overflow:hidden}
.slide-title{position:absolute;left:17px;top:8px;font-weight:400;font-size:12px;color:var(--ink);letter-spacing:.1px}
.slide-title::after{content:"";position:absolute;left:0;bottom:-2px;width:18px;height:1.5px;background:var(--red)}
.brand{position:absolute;right:14px;top:11px;font-size:6px;font-weight:600;color:var(--ink)}
.art{position:absolute;inset:0;width:345px;height:198px}
.slide-footer{position:absolute;left:0;right:0;bottom:0;height:9px;background:var(--footer);color:#fff;font-size:4px;display:flex;align-items:center;padding-left:5px}
.slide-footer .web{margin-left:auto;margin-right:6px}
.slide-footer .page{background:var(--footer-dark);height:9px;width:19px;display:flex;align-items:center;justify-content:center}
svg text{font-family:"Raleway",sans-serif}
.t{font-size:3.6px;fill:var(--muted)}
.tc{font-size:3.6px;fill:var(--muted);text-anchor:middle}
.tw{font-size:3.8px;fill:#fff;text-anchor:middle}
.h{font-size:5.6px;fill:var(--ink)}
.lbl{font-size:5.2px;text-anchor:middle;font-weight:600}
.photo{fill:#d9d9d9}
.closing{background:linear-gradient(135deg,#c2262d,#9d1118)}
.closing .panel{position:absolute;left:0;top:0;width:146px;height:198px;background:rgba(150,12,18,.85)}
.closing .name{position:absolute;left:48px;top:38px;color:#fce9a9;font-size:6px;font-weight:600}
.closing h3{position:absolute;left:38px;top:80px;color:#fff;font-weight:400;font-size:9px}
.closing h3::after{content:"";position:absolute;left:0;bottom:-3px;width:60px;height:.6px;background:rgba(255,255,255,.5)}
.closing ul{position:absolute;left:38px;top:107px;list-style:none;color:#fff;font-size:5px;line-height:6px}
.closing li{display:flex;gap:5px;margin-bottom:6px}
.closing li b{width:5px;height:5px;border-radius:50%;background:#fff;margin-top:1px;flex:none}
.closing .webbar{position:absolute;left:27px;top:182px;width:118px;height:14px;background:#111;color:#fff;font-size:5px;display:flex;align-items:center;padding-left:27px}
.closing .thanks{position:absolute;left:146px;right:0;top:92px;text-align:center;color:#fff}
.closing .thanks h2{font-size:15px;font-weight:700;letter-spacing:.3px}
.closing .thanks p{font-size:5.4px;margin-top:2px}
.closing .thanks small{display:block;font-size:4.6px;margin-top:10px;line-height:6px}
.scene{position:absolute;left:146px;top:0;right:0;height:198px;background:linear-gradient(180deg,rgba(255,255,255,.08),rgba(0,0,0,.08) 60%,rgba(255,255,255,.05))}
.team-photo{position:absolute;left:0;top:0;width:92px;height:189px;background:linear-gradient(160deg,#cfe4f2,#f2c94c 60%,#d9a62a)}
.team-photo span{position:absolute;left:0;right:0;bottom:0;height:30px;background:rgba(176,18,26,.55);color:#fff;font-size:9px;padding:10px 0 0 9px}
</style>
</head>
<body>
<main class="deck">

<section class="slide">
  <h2 class="slide-title">Global Experience</h2>
  <div class="brand">Pell Schools</div>
  <svg class="art" viewBox="0 0 345 198">
    <rect x="76" y="20" width="188" height="92" rx="4" fill="#dcdcdc" role="img" aria-label="World map with office locations"/>
    <circle cx="22" cy="147" r="5" fill="var(--red)"/>
    <text class="h" x="29" y="149">Heading Goes Here</text>
    <text class="t" x="17" y="158">Lorem ipsum dolor sit amet, consectetur adipiscing elit, sed do</text>
    <text class="t" x="17" y="163">eiusmod tempor incididunt ut labore et dolore magna aliqua</text>
  </svg>
  <footer class="slide-footer">© Copyright 2017 Pell Schools<span class="web">www.pellru8k.example</span><span class="page">34</span></footer>
</section>

<section class="slide">
  <h2 class="slide-title">Key Points Area</h2>
  <div class="brand">Pell Schools</div>
  <svg class="art" viewBox="0 0 345 198">
    <text class="t" x="22" y="46">Lorem ipsum dolor sit amet, consectetur adipiscing elit, sed do eiusmod tempor incididunt ut labore et dolore</text>
    <text class="t" x="22" y="52">magna aliqua. Ut enim ad minim veniam, quis nostrud exercitation ullamco laboris nisi ut aliquip ex ea commodo</text>
    <text class="t" x="22" y="58">consequat.</text>
    <g opacity=".93">
      <circle cx="110" cy="98" r="25" fill="var(--red)"/>
      <circle cx="151" cy="98" r="25" fill="var(--yellow)"/>
      <circle cx="192" cy="98" r="25" fill="var(--teal)"/>
      <circle cx="233" cy="98" r="25" fill="var(--green)"/>
      <circle cx="274" cy="98" r="25" fill="var(--blue)"/>
    </g>
    <g fill="#fff">
      <circle cx="110" cy="91" r="3"/><rect x="147" y="88" width="8" height="2" transform="rotate(-40 151 89)"/>
      <rect x="188" y="89" width="2" height="5"/><rect x="191" y="86" width="2" height="8"/><rect x="194" y="88" width="2" height="6"/>
      <circle cx="231" cy="90" r="2.5"/><circle cx="235" cy="90" r="2.5"/><path d="M228.7 91 L233 96 L237.3 91Z"/>
      <path d="M269 94 L270 87 L272 90 L274 86 L276 90 L278 87 L279 94Z"/>
    </g>
    <text class="tw" x="110" y="103">Lorem</text><text class="tw" x="110" y="108">ipsum</text>
    <text class="tw" x="151" y="103">Lorem</text><text class="tw" x="151" y="108">ipsum</text>
    <text class="tw" x="192" y="103">Lorem</text><text class="tw" x="192" y="108">ipsum</text>
    <text class="tw" x="233" y="103">Lorem</text><text class="tw" x="233" y="108">ipsum</text>
    <text class="tw" x="274" y="103">Lorem</text><text class="tw" x="274" y="108">ipsum</text>
    <text class="tc" x="172" y="142">Lorem ipsum dolor sit amet, consectetur adipiscing elit, sed do eiusmod tempor</text>
    <text class="tc" x="172" y="148">incididunt ut labore et dolore magna aliqua. Ut enim ad minim veniam, quis nostrud</text>
    <text class="tc" x="172" y="154">exercitation ullamco laboris nisi ut aliquip ex ea commodo consequat.</text>
  </svg>
  <footer class="slide-footer">© Copyright 2017 Pell Schools<span class="web">www.pellru8k.example</span><span class="page">35</span></footer>
</section>

<section class="slide">
  <h2 class="slide-title">Four Column Area</h2>
  <div class="brand">Pell Schools</div>
  <svg class="art" viewBox="0 0 345 198">
    <text class="h" x="29" y="47">Heading Goes Here</text>
    <text class="t" x="29" y="53">Lorem ipsum dolor sit amet, consectetur adipiscing elit, sed do eiusmod tempor incididunt ut labore et commodo</text>
    <text class="t" x="29" y="58">consequat dolore magna aliqua. Duis aute irure dolor in reprehenderit in voluptate velit esse cillum dolore eu fugiat nulla</text>
    <text class="t" x="29" y="63">pariatur.</text>
    <rect x="27" y="73" width="64" height="85" fill="var(--blue)"/>
    <rect x="103" y="73" width="64" height="85" fill="var(--green)"/>
    <rect x="178" y="73" width="64" height="85" fill="var(--orange)"/>
    <rect x="254" y="73" width="64" height="85" fill="var(--teal)"/>
    <g fill="#fff"><circle cx="59" cy="98" r="7"/><circle cx="135" cy="98" r="7"/><circle cx="210" cy="98" r="7"/><circle cx="286" cy="98" r="7"/></g>
    <g fill="none" stroke-width="1.3">
      <circle cx="59" cy="98" r="3" stroke="var(--blue)"/><circle cx="135" cy="98" r="3" stroke="var(--green)"/>
      <circle cx="210" cy="98" r="3" stroke="var(--orange)"/><circle cx="286" cy="98" r="3" stroke="var(--teal)"/>
    </g>
    <g class="tw" style="font-size:4.6px"><text x="59" y="120">COLUMN 1</text><text x="135" y="120">COLUMN 2</text><text x="210" y="120">COLUMN 3</text><text x="286" y="120">COLUMN 4</text></g>
    <g class="tw">
      <text x="59" y="130">Lorem ipsum dolor</text><text x="59" y="135">sit consectetur</text><text x="59" y="140">adipiscing elit.</text>
      <text x="135" y="130">Lorem ipsum dolor</text><text x="135" y="135">sit consectetur</text><text x="135" y="140">adipiscing elit.</text>
      <text x="210" y="130">Lorem ipsum dolor</text><text x="210" y="135">sit consectetur</text><text x="210" y="140">adipiscing elit.</text>
      <text x="286" y="130">Lorem ipsum dolor</text><text x="286" y="135">sit consectetur</text><text x="286" y="140">adipiscing elit.</text>
    </g>
  </svg>
  <footer class="slide-footer">© Copyright 2017 Pell Schools<span class="web">www.pellru8k.example</span><span class="page">36</span></footer>
</section>

<section class="slide">
  <h2 class="slide-title">Five Column Area</h2>
  <div class="brand">Pell Schools</div>
  <svg class="art" viewBox="0 0 345 198">
    <text class="t" x="23" y="40">Lorem ipsum dolor sit amet, consectetur adipiscing elit, sed do eiusmod tempor incididunt ut labore et dolore magna</text>
    <text class="t" x="23" y="46">aliqua. Ut enim ad minim veniam, quis nostrud exercitation ullamco laboris nisi ut aliquip ex ea commodo consequat.</text>
    <g fill="none" stroke-width="3.5">
      <circle cx="39" cy="93" r="19" stroke="var(--teal)"/>
      <circle cx="106" cy="93" r="19" stroke="var(--orange)"/>
      <circle cx="173" cy="93" r="19" stroke="var(--green)"/>
      <circle cx="240" cy="93" r="19" stroke="var(--red)"/>
      <circle cx="307" cy="93" r="19" stroke="var(--blue)"/>
    </g>
    <g fill="var(--teal)"><path d="M34 87h10l-2 6h-6z"/><rect x="38" y="93" width="2" height="4"/><rect x="35" y="97" width="8" height="1.5"/></g>
    <path fill="var(--orange)" d="M100 97 L101 88 L103.5 92 L106 87 L108.5 92 L111 88 L112 97Z"/>
    <path fill="var(--green)" d="M167 99 L179 87 L177 93 L181 95 L175 97 L173 101Z"/>
    <circle cx="240" cy="91" r="5" fill="var(--red)"/><path fill="var(--red)" d="M237 95 L235 100 L240 98 L245 100 L243 95Z"/>
    <g fill="var(--blue)"><rect x="301" y="94" width="2.5" height="4"/><rect x="305" y="90" width="2.5" height="8"/><rect x="309" y="87" width="2.5" height="11"/></g>
    <g class="lbl">
      <text x="39" y="122" fill="var(--teal)">COLUMN 1</text><text x="106" y="122" fill="var(--orange)">COLUMN 2</text>
      <text x="173" y="122" fill="var(--green)">COLUMN 3</text><text x="240" y="122" fill="var(--red)">COLUMN 4</text>
      <text x="307" y="122" fill="var(--blue)">COLUMN 5</text>
    </g>
    <g stroke="#e4e4e4" stroke-width=".6"><line x1="72" y1="70" x2="72" y2="168"/><line x1="139" y1="70" x2="139" y2="168"/><line x1="206" y1="70" x2="206" y2="168"/><line x1="273" y1="70" x2="273" y2="168"/></g>
    <g class="tc">
      <text x="39" y="131">Lorem ipsum dolor sit</text><text x="39" y="136">amet, consectetur</text><text x="39" y="141">adipiscing elit, sed do</text><text x="39" y="146">eiusmod tempor</text><text x="39" y="151">incididunt ut labore et</text><text x="39" y="156">dolore magna aliqua.</text>
      <text x="106" y="131">Lorem ipsum dolor sit</text><text x="106" y="136">amet, consectetur</text><text x="106" y="141">adipiscing elit, sed do</text><text x="106" y="146">eiusmod tempor</text><text x="106" y="151">incididunt ut labore et</text><text x="106" y="156">dolore magna aliqua.</text>
      <text x="173" y="131">Lorem ipsum dolor sit</text><text x="173" y="136">amet, consectetur</text><text x="173" y="141">adipiscing elit, sed do</text><text x="173" y="146">eiusmod tempor</text><text x="173" y="151">incididunt ut labore et</text><text x="173" y="156">dolore magna aliqua.</text>
      <text x="240" y="131">Lorem ipsum dolor sit</text><text x="240" y="136">amet, consectetur</text><text x="240" y="141">adipiscing elit, sed do</text><text x="240" y="146">eiusmod tempor</text><text x="240" y="151">incididunt ut labore et</text><text x="240" y="156">dolore magna aliqua.</text>
      <text x="307" y="131">Lorem ipsum dolor sit</text><text x="307" y="136">amet, consectetur</text><text x="307" y="141">adipiscing elit, sed do</text><text x="307" y="146">eiusmod tempor</text><text x="307" y="151">incididunt ut labore et</text><text x="307" y="156">dolore magna aliqua.</text>
    </g>
  </svg>
  <footer class="slide-footer">© Copyright 2017 Pell Schools<span class="web">www.pellru8k.example</span><span class="page">37</span></footer>
</section>

<section class="slide">
  <h2 class="slide-title">Five Column Area</h2>
  <div class="brand">Pell Schools</div>
  <svg class="art" viewBox="0 0 345 198">
    <text class="h" x="16" y="46">Heading Goes Here</text>
    <text class="t" x="16" y="52">Lorem ipsum dolor sit amet, consectetur adipiscing elit, sed do eiusmod tempor incididunt ut labore et commodo</text>
    <text class="t" x="16" y="57">consequat dolore magna aliqua. Duis aute irure dolor in reprehenderit in voluptate velit esse cillum dolore eu fugiat nulla</text>
    <text class="t" x="16" y="62">pariatur.</text>
    <rect x="14" y="87" width="58" height="81" fill="var(--blue)"/>
    <rect x="79" y="87" width="58" height="81" fill="var(--red)"/>
    <rect x="143" y="87" width="58" height="81" fill="var(--green)"/>
    <rect x="208" y="87" width="58" height="81" fill="var(--orange)"/>
    <rect x="273" y="87" width="58" height="81" fill="var(--blue)"/>
    <g fill="#fff"><circle cx="43" cy="106" r="6.5"/><circle cx="108" cy="106" r="6.5"/><circle cx="172" cy="106" r="6.5"/><circle cx="237" cy="106" r="6.5"/><circle cx="302" cy="106" r="6.5"/></g>
    <g class="tw" style="font-size:4.6px"><text x="43" y="126">COLUMN 1</text><text x="108" y="126">COLUMN 2</text><text x="172" y="126">COLUMN 3</text><text x="237" y="126">COLUMN 4</text><text x="302" y="126">COLUMN 5</text></g>
    <g class="tw">
      <text x="43" y="136">Lorem ipsum dolor</text><text x="43" y="141">sit consectetur</text><text x="43" y="146">adipiscing elit.</text>
      <text x="108" y="136">Lorem ipsum dolor</text><text x="108" y="141">sit consectetur</text><text x="108" y="146">adipiscing elit.</text>
      <text x="172" y="136">Lorem ipsum dolor</text><text x="172" y="141">sit consectetur</text><text x="172" y="146">adipiscing elit.</text>
      <text x="237" y="136">Lorem ipsum dolor</text><text x="237" y="141">sit consectetur</text><text x="237" y="146">adipiscing elit.</text>
      <text x="302" y="136">Lorem ipsum dolor</text><text x="302" y="141">sit consectetur</text><text x="302" y="146">adipiscing elit.</text>
    </g>
  </svg>
  <footer class="slide-footer">© Copyright 2017 Pell Schools<span class="web">www.pellru8k.example</span><span class="page">38</span></footer>
</section>

<section class="slide">
  <h2 class="slide-title">Timeline</h2>
  <div class="brand">Pell Schools</div>
  <svg class="art" viewBox="0 0 345 198">
    <line x1="60" y1="90" x2="282" y2="90" stroke="#8a8a8a" stroke-width=".8"/>
    <g stroke="#aaa" stroke-width=".6"><line x1="89" y1="76" x2="89" y2="90"/><line x1="131" y1="90" x2="131" y2="111"/><line x1="172" y1="76" x2="172" y2="90"/><line x1="214" y1="90" x2="214" y2="111"/><line x1="256" y1="76" x2="256" y2="90"/></g>
    <g fill="#666"><circle cx="89" cy="90" r="1.3"/><circle cx="131" cy="90" r="1.3"/><circle cx="172" cy="90" r="1.3"/><circle cx="214" cy="90" r="1.3"/><circle cx="256" cy="90" r="1.3"/></g>
    <circle cx="46" cy="90" r="17" fill="var(--red)"/><circle cx="89" cy="59" r="17" fill="var(--orange)"/>
    <circle cx="131" cy="128" r="17" fill="var(--blue)"/><circle cx="172" cy="59" r="17" fill="var(--green)"/>
    <circle cx="214" cy="128" r="17" fill="var(--orange)"/><circle cx="256" cy="59" r="17" fill="var(--teal)"/>
    <circle cx="296" cy="90" r="17" fill="var(--red)"/>
    <g class="tw" style="font-size:7.5px">
      <text x="46" y="91">2010</text><text x="89" y="60">2011</text><text x="131" y="129">2012</text><text x="172" y="60">2013</text><text x="214" y="129">2014</text><text x="256" y="60">2015</text><text x="296" y="91">2016</text>
    </g>
    <g class="tw" style="font-size:2.6px">
      <text x="46" y="96">Your Text</text><text x="46" y="99">Goes Here</text><text x="89" y="65">Your Text</text><text x="89" y="68">Goes Here</text>
      <text x="131" y="134">Your Text</text><text x="131" y="137">Goes Here</text><text x="172" y="65">Your Text</text><text x="172" y="68">Goes Here</text>
      <text x="214" y="134">Your Text</text><text x="214" y="137">Goes Here</text><text x="256" y="65">Your Text</text><text x="256" y="68">Goes Here</text>
      <text x="296" y="96">Your Text</text><text x="296" y="99">Goes Here</text>
    </g>
    <path d="M302 108 Q306 116 298 121" fill="none" stroke="var(--red)" stroke-width=".7"/>
    <text x="327" y="128" style="font-size:5.4px;text-anchor:end" fill="var(--red)">Your Text Goes Here</text>
    <g class="t" style="text-anchor:end"><text x="327" y="134">Lorem ipsum dolor sit amet,</text><text x="327" y="139">consectetur adipiscing elit,</text><text x="327" y="144">sed do eiusmod tempor</text><text x="327" y="149">incididunt ut labore et</text><text x="327" y="154">dolore magna aliqua</text></g>
    <text class="h" x="14" y="154">Heading Goes Here</text>
    <text class="t" x="14" y="160">Lorem ipsum dolor sit amet, consectetur adipiscing elit, sed do</text>
    <text class="t" x="14" y="165">eiusmod tempor incididunt ut labore et dolore magna aliqua</text>
  </svg>
  <footer class="slide-footer">© Copyright 2017 Pell Schools<span class="web">www.pellru8k.example</span><span class="page">39</span></footer>
</section>

<section class="slide">
  <h2 class="slide-title">Workflow Area</h2>
  <div class="brand">Pell Schools</div>
  <svg class="art" viewBox="0 0 345 198">
    <text class="t" x="26" y="50">Lorem ipsum dolor sit amet, consectetur adipiscing elit, sed do eiusmod tempor incididunt ut labore et dolore</text>
    <text class="t" x="26" y="56">magna aliqua. Ut enim ad minim veniam, quis nostrud exercitation ullamco laboris nisi ut aliquip ex ea commodo</text>
    <text class="t" x="26" y="62">consequat.</text>
    <g fill="none" stroke-width="10">
      <path d="M22 125 A36 36 0 0 1 94 125" stroke="var(--red)"/>
      <path d="M94 125 A21 21 0 0 0 136 125" stroke="#8cc63f"/>
      <path d="M136 125 A36 36 0 0 1 208 125" stroke="var(--red)"/>
      <path d="M208 125 A21 21 0 0 0 250 125" stroke="#8cc63f"/>
      <path d="M250 125 A36 36 0 0 1 322 125" stroke="var(--red)"/>
    </g>
    <g fill="var(--red)" stroke="#fff" stroke-width="1"><circle cx="58" cy="104" r="5"/><circle cx="172" cy="104" r="5"/><circle cx="286" cy="104" r="5"/></g>
    <g fill="#8cc63f" stroke="#fff" stroke-width="1"><circle cx="115" cy="146" r="5"/><circle cx="229" cy="146" r="5"/></g>
    <g class="tw" style="font-size:3.6px"><text x="58" y="105.5">1</text><text x="115" y="147.5">2</text><text x="172" y="105.5">3</text><text x="229" y="147.5">4</text><text x="286" y="105.5">5</text></g>
    <g class="lbl" style="font-size:5.6px">
      <text x="58" y="120" fill="var(--red)">Data 1</text><text x="115" y="83" fill="#8cc63f">Data 2</text>
      <text x="172" y="120" fill="var(--red)">Data 3</text><text x="229" y="83" fill="#8cc63f">Data 4</text>
      <text x="286" y="120" fill="var(--red)">Data 5</text>
    </g>
    <g class="tc">
      <text x="58" y="129">Lorem ipsum</text><text x="58" y="134">dolor sit amet,</text><text x="58" y="139">consectetur</text><text x="58" y="144">adipiscing elit.</text>
      <text x="115" y="91">Lorem ipsum</text><text x="115" y="96">dolor sit amet,</text><text x="115" y="101">consectetur</text><text x="115" y="106">adipiscing elit.</text>
      <text x="172" y="129">Lorem ipsum</text><text x="172" y="134">dolor sit amet,</text><text x="172" y="139">consectetur</text><text x="172" y="144">adipiscing elit.</text>
      <text x="229" y="91">Lorem ipsum</text><text x="229" y="96">dolor sit amet,</text><text x="229" y="101">consectetur</text><text x="229" y="106">adipiscing elit.</text>
      <text x="286" y="129">Lorem ipsum</text><text x="286" y="134">dolor sit amet,</text><text x="286" y="139">consectetur</text><text x="286" y="144">adipiscing elit.</text>
    </g>
  </svg>
  <footer class="slide-footer">© Copyright 2017 Pell Schools<span class="web">www.pellru8k.example</span><span class="page">40</span></footer>
</section>

<section class="slide">
  <h2 class="slide-title">Steps Process Area</h2>
  <div class="brand">Pell Schools</div>
  <svg class="art" viewBox="0 0 345 198">
    <text class="h" x="15" y="58">Heading Goes Here</text>
    <text class="t" x="15" y="64">Lorem ipsum dolor sit amet, consectetur</text>
    <text class="t" x="15" y="69">adipiscing elit, sed do eiusmod tempor</text>
    <text class="t" x="15" y="74">incididunt ut labore</text>
    <g stroke-width="5" fill="none"><line x1="178" y1="120" x2="205" y2="126" stroke="var(--red)"/><line x1="226" y1="103" x2="224" y2="115" stroke="var(--orange)"/></g>
    <g fill="#fff" stroke-width="4">
      <circle cx="165" cy="102" r="24" stroke="var(--red)"/>
      <circle cx="235" cy="86" r="17" stroke="var(--orange)"/>
      <circle cx="220" cy="133" r="20" stroke="#8cc63f"/>
      <circle cx="264" cy="135" r="23" stroke="var(--blue)"/>
    </g>
    <path fill="var(--red)" d="M156 111 L172 93 L174 92 L173 96 L160 113Z"/><circle cx="162" cy="106" r="2" fill="var(--red)"/>
    <g fill="var(--orange)"><rect x="229" y="88" width="2.5" height="4"/><rect x="233" y="85" width="2.5" height="7"/><rect x="237" y="82" width="2.5" height="10"/></g>
    <circle cx="220" cy="133" r="6" fill="none" stroke="#8cc63f" stroke-width="3" stroke-dasharray="2 1.5"/>
    <path fill="var(--blue)" d="M256 140 L257 130 L260 134 L264 128 L268 134 L271 130 L272 140Z"/>
    <g style="font-size:5px"><text x="106" y="100" fill="var(--red)">Step 01</text><text x="122" y="146" fill="#8cc63f">Step 02</text><text x="247" y="58" fill="var(--orange)">Step 03</text><text x="295" y="132" fill="var(--blue)">Step 04</text></g>
    <g class="t">
      <text x="97" y="106">Lorem ipsum dolor</text><text x="97" y="111">sit amet, consectetur</text><text x="97" y="116">adipiscing elit, sed</text><text x="97" y="121">do eiusmod tempor</text>
      <text x="113" y="152">Lorem ipsum dolor</text><text x="113" y="157">sit amet, consectetur</text><text x="113" y="162">adipiscing elit, sed</text><text x="113" y="167">do eiusmod tempor</text>
      <text x="247" y="64">Lorem ipsum dolor sit</text><text x="247" y="69">amet consectetur</text><text x="247" y="74">adipiscing elit sed do</text><text x="247" y="79">eiusmod tempor</text>
      <text x="295" y="138">Lorem ipsum</text><text x="295" y="143">dolor sit amet,</text><text x="295" y="148">consectetur</text><text x="295" y="153">adipiscing elit</text>
    </g>
  </svg>
  <footer class="slide-footer">© Copyright 2017 Pell Schools<span class="web">www.pellru8k.example</span><span class="page">41</span></footer>
</section>

<section class="slide">
  <h2 class="slide-title">Steps Process Area</h2>
  <div class="brand">Pell Schools</div>
  <svg class="art" viewBox="0 0 345 198">
    <text class="h" x="15" y="45">Heading Goes Here</text>
    <g class="t"><text x="15" y="51">Lorem ipsum dolor sit amet,</text><text x="15" y="56">consectetur adipiscing elit, sed do</text><text x="15" y="61">eiusmod tempor incididunt ut</text><text x="15" y="66">labore</text></g>
    <path d="M202 22 C202 32 194 30 194 41 C180 41 180 64 194 64 C208 64 208 87 194 87 C180 87 180 110 194 110 C208 110 208 133 194 133 C180 133 180 155 194 155 C208 155 208 170 198 176" fill="none" stroke="var(--orange)" stroke-width="4"/>
    <g stroke="#8cc63f" stroke-width="2">
      <line x1="200" y1="41" x2="248" y2="41"/><line x1="188" y1="64" x2="150" y2="64"/><line x1="200" y1="87" x2="248" y2="87"/>
      <line x1="188" y1="110" x2="150" y2="110"/><line x1="200" y1="133" x2="248" y2="133"/><line x1="188" y1="155" x2="150" y2="155"/>
    </g>
    <g fill="#fff" stroke="#8cc63f" stroke-width="1.5">
      <circle cx="194" cy="41" r="5"/><circle cx="194" cy="64" r="5"/><circle cx="194" cy="87" r="5"/><circle cx="194" cy="110" r="5"/><circle cx="194" cy="133" r="5"/><circle cx="194" cy="155" r="5"/>
      <circle cx="249" cy="41" r="1.5"/><circle cx="149" cy="64" r="1.5"/><circle cx="249" cy="87" r="1.5"/><circle cx="149" cy="110" r="1.5"/><circle cx="249" cy="133" r="1.5"/><circle cx="149" cy="155" r="1.5"/>
    </g>
    <g style="font-size:3.4px;text-anchor:middle" fill="#8cc63f"><text x="194" y="42.3">01</text><text x="194" y="65.3">02</text><text x="194" y="88.3">03</text><text x="194" y="111.3">04</text><text x="194" y="134.3">05</text><text x="194" y="156.3">06</text></g>
    <g style="font-size:5px" fill="#444"><text x="254" y="37">Step 01</text><text x="254" y="83">Step 03</text><text x="254" y="129">Step 05</text></g>
    <g style="font-size:5px;text-anchor:end" fill="#444"><text x="144" y="60">Step 02</text><text x="144" y="106">Step 04</text><text x="144" y="151">Step 06</text></g>
    <g class="t">
      <text x="254" y="42">Lorem ipsum dolor sit amet,</text><text x="254" y="46">consectetur adipiscing elit</text><text x="254" y="50">sed do eiusmod tempor</text>
      <text x="254" y="88">Lorem ipsum dolor sit amet,</text><text x="254" y="92">consectetur adipiscing elit</text><text x="254" y="96">sed do eiusmod tempor</text>
      <text x="254" y="134">Lorem ipsum dolor sit amet,</text><text x="254" y="138">consectetur adipiscing elit</text><text x="254" y="142">sed do eiusmod tempor</text>
    </g>
    <g class="t" style="text-anchor:end">
      <text x="144" y="65">Lorem ipsum dolor sit amet,</text><text x="144" y="69">consectetur adipiscing elit</text><text x="144" y="73">sed do eiusmod tempor</text>
      <text x="144" y="111">Lorem ipsum dolor sit amet,</text><text x="144" y="115">consectetur adipiscing elit</text><text x="144" y="119">sed do eiusmod tempor</text>
      <text x="144" y="160">Lorem ipsum dolor sit amet,</text><text x="144" y="164">consectetur adipiscing elit</text><text x="144" y="168">sed do eiusmod tempor</text>
    </g>
  </svg>
  <footer class="slide-footer">© Copyright 2017 Pell Schools<span class="web">www.pellru8k.example</span><span class="page">42</span></footer>
</section>

<section class="slide">
  <h2 class="slide-title">Bullet &amp; Chart Area</h2>
  <div class="brand">Pell Schools</div>
  <svg class="art" viewBox="0 0 345 198">
    <path d="M89 101 L89 59 A42 42 0 1 1 74.6 140.5Z" fill="var(--orange)"/>
    <path d="M89 101 L74.6 140.5 A42 42 0 0 1 47.6 93.7Z" fill="var(--red)"/>
    <path d="M89 101 L47.6 93.7 A42 42 0 0 1 71.2 63Z" fill="var(--blue)"/>
    <path d="M89 101 L71.2 63 A42 42 0 0 1 89 59Z" fill="#8cc63f"/>
    <text x="58" y="56" style="font-size:10px" fill="var(--blue)">10%</text>
    <text x="22" y="85" style="font-size:10px" fill="var(--orange)">15%</text>
    <text x="22" y="137" style="font-size:10px" fill="var(--red)">25%</text>
    <text x="136" y="110" style="font-size:11px" fill="#333">60%</text>
    <g style="font-size:3px" fill="#999"><circle cx="51" cy="153" r="1" fill="var(--orange)"/><text x="53" y="154">1st Qtr</text><circle cx="69" cy="153" r="1" fill="var(--red)"/><text x="71" y="154">2nd Qtr</text><circle cx="88" cy="153" r="1" fill="var(--blue)"/><text x="90" y="154">3rd Qtr</text><circle cx="106" cy="153" r="1" fill="#8cc63f"/><text x="108" y="154">4th Qtr</text></g>
    <g><circle cx="195" cy="57" r="7" fill="var(--red)"/><circle cx="195" cy="85" r="7" fill="#8cc63f"/><circle cx="195" cy="113" r="7" fill="var(--orange)"/><circle cx="195" cy="141" r="7" fill="var(--blue)"/></g>
    <g fill="none" stroke="#fff" stroke-width="1.2"><circle cx="194" cy="56" r="2.2"/><line x1="195.6" y1="57.6" x2="197.5" y2="59.5"/><line x1="192" y1="88" x2="198" y2="82"/><line x1="193" y1="116" x2="198" y2="110"/><circle cx="195" cy="141" r="2.5" stroke-dasharray="1.5 1"/></g>
    <g style="font-size:6px"><text x="210" y="58" fill="var(--red)">Category One</text><text x="210" y="86" fill="#8cc63f">Category Two</text><text x="210" y="114" fill="var(--orange)">Category Three</text><text x="210" y="142" fill="var(--blue)">Category Four</text></g>
    <g class="t">
      <text x="210" y="64">Lorem ipsum dolor sit amet, consectetur</text><text x="210" y="68">adipiscing elit, sed do eiusmod</text>
      <text x="210" y="92">Lorem ipsum dolor sit amet, consectetur</text><text x="210" y="96">adipiscing elit, sed do eiusmod</text>
      <text x="210" y="120">Lorem ipsum dolor sit amet, consectetur</text><text x="210" y="124">adipiscing elit, sed do eiusmod</text>
      <text x="210" y="148">Lorem ipsum dolor sit amet, consectetur</text><text x="210" y="152">adipiscing elit, sed do eiusmod</text>
    </g>
  </svg>
  <footer class="slide-footer">© Copyright 2017 Pell Schools<span class="web">www.pellru8k.example</span><span class="page">43</span></footer>
</section>

<section class="slide">
  <h2 class="slide-title" style="color:var(--blue)">Table Area</h2>
  <div class="brand">Pell Schools</div>
  <svg class="art" viewBox="0 0 345 198">
    <rect x="52" y="44" width="238" height="122" fill="#fff" stroke="#eee"/>
    <rect x="52" y="44" width="96" height="30" fill="var(--orange)"/>
    <rect x="148" y="44" width="72" height="28" fill="#8cc63f"/>
    <rect x="220" y="44" width="70" height="28" fill="var(--teal)"/>
    <text x="58" y="62" style="font-size:5.4px;font-weight:600" fill="#fff">Description</text>
    <text x="184" y="55" class="tw" style="font-size:5.2px;font-weight:600">Column 1</text>
    <text x="255" y="55" class="tw" style="font-size:5.2px;font-weight:600">Column 2</text>
    <circle cx="184" cy="65" r="4" fill="#fff"/><circle cx="255" cy="65" r="4" fill="#fff"/>
    <line x1="148" y1="74" x2="148" y2="166" stroke="#e3e3e3" stroke-width=".6"/>
    <line x1="220" y1="74" x2="220" y2="166" stroke="#e3e3e3" stroke-width=".6"/>
    <g stroke="#ddd" stroke-width=".5">
      <line x1="57" y1="98" x2="144" y2="98"/><line x1="57" y1="107" x2="144" y2="107"/><line x1="57" y1="116" x2="144" y2="116"/><line x1="57" y1="124" x2="144" y2="124"/><line x1="57" y1="133" x2="144" y2="133"/><line x1="57" y1="141" x2="144" y2="141"/><line x1="57" y1="150" x2="144" y2="150"/>
      <line x1="156" y1="98" x2="212" y2="98"/><line x1="156" y1="107" x2="212" y2="107"/><line x1="156" y1="116" x2="212" y2="116"/><line x1="156" y1="124" x2="212" y2="124"/><line x1="156" y1="133" x2="212" y2="133"/><line x1="156" y1="141" x2="212" y2="141"/><line x1="156" y1="150" x2="212" y2="150"/>
      <line x1="228" y1="98" x2="284" y2="98"/><line x1="228" y1="107" x2="284" y2="107"/><line x1="228" y1="116" x2="284" y2="116"/><line x1="228" y1="124" x2="284" y2="124"/><line x1="228" y1="133" x2="284" y2="133"/><line x1="228" y1="141" x2="284" y2="141"/><line x1="228" y1="150" x2="284" y2="150"/>
    </g>
    <g style="font-size:3.3px" fill="#555">
      <text x="57" y="96">Description 1</text><text x="57" y="105">Description 2</text><text x="57" y="114">Description 3</text><text x="57" y="122">Description 4</text><text x="57" y="131">Description 5</text><text x="57" y="139">Description 6</text><text x="57" y="148">Description 7</text><text x="57" y="156">Description 8</text>
    </g>
    <g fill="#222"><circle cx="184" cy="94" r="1.2"/><circle cx="184" cy="103" r="1.2"/><circle cx="184" cy="112" r="1.2"/><circle cx="184" cy="120" r="1.2"/><circle cx="184" cy="155" r="1.2"/>
      <circle cx="255" cy="94" r="1.2"/><circle cx="255" cy="103" r="1.2"/><circle cx="255" cy="112" r="1.2"/><circle cx="255" cy="120" r="1.2"/><circle cx="255" cy="155" r="1.2"/></g>
    <g style="font-size:3.2px;text-anchor:middle" fill="#555"><text x="184" y="131">Text Column 1</text><text x="184" y="147">Text Column 1</text><text x="255" y="131">Text Column 2</text><text x="255" y="147">Text Column 2</text></g>
  </svg>
  <footer class="slide-footer">© Copyright 2017 Pell Schools<span class="web">www.pellru8k.example</span><span class="page">44</span></footer>
</section>

<section class="slide">
  <h2 class="slide-title">Bullet &amp; Chart Area</h2>
  <div class="brand">Pell Schools</div>
  <svg class="art" viewBox="0 0 345 198">
    <g><circle cx="41" cy="57" r="7" fill="var(--teal)"/><circle cx="41" cy="85" r="7" fill="var(--orange)"/><circle cx="41" cy="113" r="7" fill="var(--red)"/><circle cx="41" cy="141" r="7" fill="var(--blue)"/></g>
    <g fill="none" stroke="#fff" stroke-width="1.2"><circle cx="40" cy="56" r="2.2"/><line x1="41.6" y1="57.6" x2="43.5" y2="59.5"/><line x1="38" y1="88" x2="44" y2="82"/><line x1="39" y1="116" x2="44" y2="110"/><circle cx="41" cy="141" r="2.5" stroke-dasharray="1.5 1"/></g>
    <g style="font-size:6px"><text x="56" y="58" fill="#444">Your Text Here</text><text x="56" y="86" fill="var(--red)">Your Text Here</text><text x="56" y="114" fill="var(--orange)">Your Text Here</text><text x="56" y="142" fill="var(--blue)">Your Text Here</text></g>
    <g class="t">
      <text x="56" y="64">Lorem ipsum dolor sit amet, consectetur</text><text x="56" y="68">adipiscing elit, sed do eiusmod</text>
      <text x="56" y="92">Lorem ipsum dolor sit amet, consectetur</text><text x="56" y="96">adipiscing elit, sed do eiusmod</text>
      <text x="56" y="120">Lorem ipsum dolor sit amet, consectetur</text><text x="56" y="124">adipiscing elit, sed do eiusmod</text>
      <text x="56" y="148">Lorem ipsum dolor sit amet, consectetur</text><text x="56" y="152">adipiscing elit, sed do eiusmod</text>
    </g>
    <g fill="none" stroke-width="8" transform="rotate(-90 249 101)">
      <circle cx="249" cy="101" r="38" pathLength="100" stroke="var(--teal)" stroke-dasharray="57 43"/>
      <circle cx="249" cy="101" r="38" pathLength="100" stroke="var(--red)" stroke-dasharray="24 76" stroke-dashoffset="-57"/>
      <circle cx="249" cy="101" r="38" pathLength="100" stroke="var(--orange)" stroke-dasharray="11 89" stroke-dashoffset="-81"/>
      <circle cx="249" cy="101" r="38" pathLength="100" stroke="var(--blue)" stroke-dasharray="8 92" stroke-dashoffset="-92"/>
    </g>
    <g fill="#555"><rect x="236" y="105" width="4" height="5"/><rect x="242" y="99" width="4" height="11"/><rect x="248" y="93" width="4" height="17"/><rect x="254" y="86" width="4" height="24"/></g>
    <text x="231" y="56" style="font-size:10px" fill="var(--blue)">10%</text>
    <text x="192" y="81" style="font-size:10px" fill="var(--orange)">15%</text>
    <text x="192" y="131" style="font-size:10px" fill="var(--red)">25%</text>
    <text x="293" y="106" style="font-size:11px" fill="var(--teal)">60%</text>
    <g style="font-size:3px" fill="#999"><circle cx="212" cy="153" r="1" fill="var(--teal)"/><text x="214" y="154">1st Qtr</text><circle cx="230" cy="153" r="1" fill="var(--red)"/><text x="232" y="154">2nd Qtr</text><circle cx="249" cy="153" r="1" fill="var(--orange)"/><text x="251" y="154">3rd Qtr</text><circle cx="267" cy="153" r="1" fill="var(--blue)"/><text x="269" y="154">4th Qtr</text></g>
  </svg>
  <footer class="slide-footer">© Copyright 2017 Pell Schools<span class="web">www.pellru8k.example</span><span class="page">45</span></footer>
</section>

<section class="slide">
  <h2 class="slide-title">Bullet &amp; Chart Area</h2>
  <div class="brand">Pell Schools</div>
  <svg class="art" viewBox="0 0 345 198">
    <g style="font-size:3.4px;text-anchor:end" fill="#555"><text x="48" y="68">Category 4</text><text x="48" y="93">Category 3</text><text x="48" y="118">Category 2</text><text x="48" y="143">Category 1</text></g>
    <line x1="52" y1="58" x2="52" y2="152" stroke="#ddd" stroke-width=".5"/>
    <g>
      <rect x="76" y="62" width="69" height="3.6" fill="var(--red)"/><rect x="76" y="66" width="40" height="3.6" fill="var(--orange)"/><rect x="76" y="70" width="60" height="3.6" fill="var(--teal)"/>
      <rect x="76" y="87" width="32" height="3.6" fill="var(--red)"/><rect x="76" y="91" width="36" height="3.6" fill="var(--orange)"/><rect x="76" y="95" width="41" height="3.6" fill="var(--teal)"/>
      <rect x="76" y="112" width="20" height="3.6" fill="var(--red)"/><rect x="76" y="116" width="58" height="3.6" fill="var(--orange)"/><rect x="76" y="120" width="45" height="3.6" fill="var(--teal)"/>
      <rect x="76" y="137" width="25" height="3.6" fill="var(--red)"/><rect x="76" y="141" width="21" height="3.6" fill="var(--orange)"/><rect x="76" y="145" width="56" height="3.6" fill="var(--teal)"/>
    </g>
    <g style="font-size:3px" fill="#999"><rect x="64" y="155" width="2" height="2" fill="var(--red)"/><text x="67" y="157">Series 3</text><rect x="86" y="155" width="2" height="2" fill="var(--orange)"/><text x="89" y="157">Series 2</text><rect x="108" y="155" width="2" height="2" fill="var(--teal)"/><text x="111" y="157">Series 1</text></g>
    <g><circle cx="195" cy="57" r="7" fill="var(--red)"/><circle cx="195" cy="85" r="7" fill="var(--teal)"/><circle cx="195" cy="113" r="7" fill="var(--orange)"/><circle cx="195" cy="141" r="7" fill="var(--blue)"/></g>
    <g fill="none" stroke="#fff" stroke-width="1.2"><circle cx="194" cy="56" r="2.2"/><line x1="195.6" y1="57.6" x2="197.5" y2="59.5"/><line x1="192" y1="88" x2="198" y2="82"/><line x1="193" y1="116" x2="198" y2="110"/><circle cx="195" cy="141" r="2.5" stroke-dasharray="1.5 1"/></g>
    <g style="font-size:6px"><text x="210" y="58" fill="var(--red)">Category One</text><text x="210" y="86" fill="var(--teal)">Category Two</text><text x="210" y="114" fill="var(--orange)">Category Three</text><text x="210" y="142" fill="var(--blue)">Category Four</text></g>
    <g class="t">
      <text x="210" y="64">Lorem ipsum dolor sit amet, consectetur</text><text x="210" y="68">adipiscing elit, sed do eiusmod</text>
      <text x="210" y="92">Lorem ipsum dolor sit amet, consectetur</text><text x="210" y="96">adipiscing elit, sed do eiusmod</text>
      <text x="210" y="120">Lorem ipsum dolor sit amet, consectetur</text><text x="210" y="124">adipiscing elit, sed do eiusmod</text>
      <text x="210" y="148">Lorem ipsum dolor sit amet, consectetur</text><text x="210" y="152">adipiscing elit, sed do eiusmod</text>
    </g>
  </svg>
  <footer class="slide-footer">© Copyright 2017 Pell Schools<span class="web">www.pellru8k.example</span><span class="page">46</span></footer>
</section>

<section class="slide">
  <h2 class="slide-title">Bullet &amp; Chart Area</h2>
  <div class="brand">Pell Schools</div>
  <svg class="art" viewBox="0 0 345 198">
    <text x="11" y="73" style="font-size:4.4px;font-weight:700" fill="#333">Lorem ipsum <tspan font-weight="400">consectetur adipiscing elit,</tspan></text>
    <text x="11" y="79" style="font-size:4.4px" fill="#333">sed do eiusmod tempor incididunt</text>
    <g><circle cx="15" cy="98" r="6" fill="var(--teal)"/><circle cx="15" cy="126" r="6" fill="var(--blue)"/><circle cx="241" cy="55" r="6" fill="var(--red)"/><circle cx="241" cy="83" r="6" fill="#8cc63f"/></g>
    <g fill="none" stroke="#fff" stroke-width="1.1"><line x1="12" y1="101" x2="18" y2="95"/><circle cx="15" cy="126" r="2.4" stroke-dasharray="1.5 1"/><circle cx="240" cy="54" r="2"/><line x1="241.5" y1="55.5" x2="243.3" y2="57.3"/><line x1="238" y1="86" x2="244" y2="80"/></g>
    <g style="font-size:6px"><text x="26" y="99" fill="var(--teal)">Category Three</text><text x="26" y="127" fill="var(--blue)">Category Four</text><text x="251" y="56" fill="var(--red)">Category One</text><text x="251" y="84" fill="#8cc63f">Category Two</text></g>
    <g class="t">
      <text x="26" y="104">Lorem ipsum dolor sit amet, consectetur</text><text x="26" y="108">adipiscing elit, sed do eiusmod</text>
      <text x="26" y="132">Lorem ipsum dolor sit amet, consectetur</text><text x="26" y="136">adipiscing elit, sed do eiusmod</text>
      <text x="251" y="61">Lorem ipsum dolor sit amet, consectetur</text><text x="251" y="65">adipiscing elit, sed do eiusmod</text>
      <text x="251" y="89">Lorem ipsum dolor sit amet, consectetur</text><text x="251" y="93">adipiscing elit, sed do eiusmod</text>
    </g>
    <line x1="150" y1="115" x2="228" y2="115" stroke="#ccc" stroke-width=".5"/>
    <g>
      <rect x="152" y="78" width="5" height="37" fill="var(--teal)"/><rect x="158" y="85" width="5" height="30" fill="#8cc63f"/><rect x="164" y="70" width="5" height="45" fill="var(--red)"/>
      <rect x="172" y="82" width="5" height="33" fill="var(--teal)"/><rect x="178" y="68" width="5" height="47" fill="#8cc63f"/><rect x="184" y="76" width="5" height="39" fill="var(--red)"/>
      <rect x="192" y="74" width="5" height="41" fill="var(--teal)"/><rect x="198" y="80" width="5" height="35" fill="#8cc63f"/><rect x="204" y="64" width="5" height="51" fill="var(--red)"/>
      <rect x="212" y="84" width="5" height="31" fill="var(--teal)"/><rect x="218" y="72" width="5" height="43" fill="#8cc63f"/><rect x="224" y="60" width="5" height="55" fill="var(--red)"/>
    </g>
    <g style="font-size:3px;text-anchor:middle" fill="#666"><text x="160" y="121">Category 1</text><text x="180" y="121">Category 2</text><text x="200" y="121">Category 3</text><text x="220" y="121">Category 4</text></g>
    <g style="font-size:3px" fill="#999"><rect x="158" y="136" width="2" height="2" fill="var(--teal)"/><text x="161" y="138">Series 1</text><rect x="180" y="136" width="2" height="2" fill="#8cc63f"/><text x="183" y="138">Series 2</text><rect x="202" y="136" width="2" height="2" fill="var(--red)"/><text x="205" y="138">Series 3</text></g>
  </svg>
  <footer class="slide-footer">© Copyright 2017 Pell Schools<span class="web">www.pellru8k.example</span><span class="page">47</span></footer>
</section>

<section class="slide">
  <h2 class="slide-title">Bullet &amp; Chart Area</h2>
  <div class="brand">Pell Schools</div>
  <svg class="art" viewBox="0 0 345 198">
    <g><circle cx="41" cy="78" r="7" fill="#8cc63f"/><circle cx="41" cy="106" r="7" fill="var(--red)"/><circle cx="41" cy="134" r="7" fill="var(--teal)"/></g>
    <g fill="none" stroke="#fff" stroke-width="1.2"><circle cx="40" cy="77" r="2.2"/><line x1="41.6" y1="78.6" x2="43.5" y2="80.5"/><line x1="38" y1="109" x2="44" y2="103"/><line x1="39" y1="137" x2="44" y2="131"/></g>
    <g style="font-size:6px"><text x="56" y="79" fill="#8cc63f">Your Text Here</text><text x="56" y="107" fill="var(--red)">Your Text Here</text><text x="56" y="135" fill="var(--teal)">Your Text Here</text></g>
    <g class="t">
      <text x="56" y="85">Lorem ipsum dolor sit amet, consectetur</text><text x="56" y="89">adipiscing elit, sed do eiusmod</text>
      <text x="56" y="113">Lorem ipsum dolor sit amet, consectetur</text><text x="56" y="117">adipiscing elit, sed do eiusmod</text>
      <text x="56" y="141">Lorem ipsum dolor sit amet, consectetur</text><text x="56" y="145">adipiscing elit, sed do eiusmod</text>
    </g>
    <line x1="184" y1="150" x2="333" y2="150" stroke="#ccc" stroke-width=".5"/>
    <g>
      <rect x="190" y="86" width="7" height="64" fill="#8cc63f"/><rect x="198" y="121" width="7" height="29" fill="var(--red)"/><rect x="206" y="116" width="7" height="34" fill="var(--teal)"/>
      <rect x="226" y="113" width="7" height="37" fill="#8cc63f"/><rect x="234" y="81" width="7" height="69" fill="var(--red)"/><rect x="242" y="117" width="7" height="33" fill="var(--teal)"/>
      <rect x="262" y="104" width="7" height="46" fill="#8cc63f"/><rect x="270" y="127" width="7" height="23" fill="var(--red)"/><rect x="278" y="106" width="7" height="44" fill="var(--teal)"/>
      <rect x="298" y="83" width="7" height="67" fill="#8cc63f"/><rect x="306" y="111" width="7" height="39" fill="var(--red)"/><rect x="314" y="74" width="7" height="76" fill="var(--teal)"/>
    </g>
    <g style="font-size:3.2px;text-anchor:middle" fill="#666"><text x="201" y="156">Category 1</text><text x="237" y="156">Category 2</text><text x="273" y="156">Category 3</text><text x="309" y="156">Category 4</text></g>
    <g style="font-size:3px" fill="#999"><rect x="228" y="159" width="2" height="2" fill="#8cc63f"/><text x="231" y="161">Series 1</text><rect x="250" y="159" width="2" height="2" fill="var(--red)"/><text x="253" y="161">Series 2</text><rect x="272" y="159" width="2" height="2" fill="var(--teal)"/><text x="275" y="161">Series 3</text></g>
  </svg>
  <footer class="slide-footer">© Copyright 2017 Pell Schools<span class="web">www.pellru8k.example</span><span class="page">48</span></footer>
</section>

<section class="slide">
  <div class="team-photo" role="img" aria-label="Photo of a student in a graduation cap"><span>Meet Our Team</span></div>
  <div class="brand">Pell Schools</div>
  <svg class="art" viewBox="0 0 345 198">
    <circle cx="132" cy="34" r="23" class="photo" role="img" aria-label="Portrait of the president"/>
    <text x="163" y="33" style="font-size:6.4px" fill="#555">Owen Hale</text>
    <text x="163" y="39" style="font-size:4.4px" fill="var(--red)">President &amp; CEO</text>
    <text x="163" y="43" style="font-size:3px" fill="#aaa">name@mail.example</text>
    <g class="photo">
      <circle cx="185" cy="86" r="16" role="img" aria-label="Portrait of VP Marketing"/>
      <circle cx="276" cy="86" r="16" role="img" aria-label="Portrait of VP Finance"/>
      <circle cx="185" cy="145" r="16" role="img" aria-label="Portrait of VP Business Development"/>
      <circle cx="276" cy="145" r="16" role="img" aria-label="Portrait of Marketing Manager"/>
    </g>
    <g style="font-size:5px;text-anchor:middle" fill="#555"><text x="185" y="110">Reed Calder</text><text x="276" y="110">Milo Brandt</text><text x="185" y="169">Tessa Lark</text><text x="276" y="169">Nora Finch</text></g>
    <g style="font-size:3.6px;text-anchor:middle" fill="var(--red)"><text x="185" y="114">VP Marketing</text><text x="276" y="114">VP Finance</text><text x="185" y="173">VP of Business Development</text><text x="276" y="173">Manager Marketing</text></g>
    <g style="font-size:3px;text-anchor:middle" fill="#aaa"><text x="185" y="118">name@mail.example</text><text x="276" y="118">name@mail.example</text><text x="185" y="177">name@mail.example</text><text x="276" y="177">name@mail.example</text></g>
  </svg>
  <footer class="slide-footer">© Copyright 2017 Pell Schools<span class="web">www.pellru8k.example</span><span class="page">49</span></footer>
</section>

<section class="slide">
  <h2 class="slide-title">Your Blank Page</h2>
  <div class="brand">Pell Schools</div>
  <svg class="art" viewBox="0 0 345 198">
    <defs><linearGradient id="faint" x1="0" y1="0" x2="0" y2="1"><stop offset="0" stop-color="#f1f1f1" stop-opacity="0"/><stop offset="1" stop-color="#ececec"/></linearGradient></defs>
    <rect x="60" y="70" width="225" height="119" fill="url(#faint)" role="img" aria-label="Faint mountain scene background"/>
  </svg>
  <footer class="slide-footer">© Copyright 2017 Pell Schools<span class="web">www.pellru8k.example</span><span class="page">50</span></footer>
</section>

<section class="slide closing">
  <div class="scene" role="img" aria-label="Rocky mountain scene in red tones"></div>
  <div class="panel"></div>
  <div class="name">Pell Schools</div>
  <h3>Our Contact</h3>
  <ul>
    <li><b></b><span>Pell County School District<br>RU-8K Harbrook-Denning</span></li>
    <li><b></b><span>(555) 014-2290</span></li>
    <li><b></b><span>listen@pellru8k.example</span></li>
  </ul>
  <div class="webbar">www.pellru8k.example</div>
  <div class="thanks">
    <h2>THANK YOU</h2>
    <p>For Your Precious Time</p>
    <small>Stop by our office or please give us a call<br>We would love to hear from you</small>
  </div>
</section>

</main>
</body>
</html>
```